Boutique Financial Services/Advisor Business Needs Web Design

Looking for an informational and functional web design for my Financial Services/Financial Advisement business. It should have functionality for Company name, address, phone #, "About Us", Who we are, Our Mission, Services we offer, Biographies/Photos of/about "The Team", and possibly a link to "Contact Us". Would like to see something new & exciting blended with a traditional/professional look that will appeal to those approaching retirement, as well as those younger clients that are beginning to think about planning for the future. I already have a web domain through HostMeadow, but would like this to be the design we use for that domain.
Financial Services/Financial Advisor
Coded - Design and coding required
1 page

```html
<!DOCTYPE html>
<html lang="en">
<head>
<meta charset="utf-8">
<title>Summitline Wealth Management</title>
<link href="https://fonts.googleapis.com/css2?family=Libre+Baskerville:wght@400;700&family=Josefin+Sans:wght@400;600;700&family=Lato:wght@400;700&display=swap" rel="stylesheet">
<style>
:root{
  --navy:#0b0a4f;
  --navy-deep:#07063d;
  --grey:#9c9c9c;
  --grey-light:#b4b4b4;
  --ink:#1d1d2b;
  --muted:#777;
  --white:#fff;
  --hero-dark:#2b2f33;
}
*{margin:0;padding:0;box-sizing:border-box}
html,body{width:1200px;height:4015px;overflow:hidden;background:var(--white)}
body{position:relative;font-family:"Lato",sans-serif;color:var(--ink)}
.abs{position:absolute}
.serif{font-family:"Libre Baskerville",serif}
.josefin{font-family:"Josefin Sans",sans-serif}

/* header */
.top-rule{left:0;top:0;width:1200px;height:5px;background:var(--navy)}
.topbar{left:0;top:0;width:1200px;height:50px}
.topbar-info{top:14px;left:560px;color:var(--white);font-size:14px;display:flex;gap:22px;align-items:center}
.topbar-info .sep{opacity:.7}
.topbar-social{display:flex;gap:10px}
.dot-s{width:12px;height:12px;border-radius:50%;background:var(--white)}
.brand{left:112px;top:30px;width:170px;text-align:center;color:var(--navy)}
.brand-mark{width:16px;height:16px;background:var(--navy);margin:0 auto 6px}
.brand-name{font-family:"Libre Baskerville",serif;font-size:14px;line-height:16px;letter-spacing:.5px}
.nav{top:79px;left:399px;display:flex;gap:0;font-family:"Libre Baskerville",serif;font-size:13px;color:var(--ink)}
.nav a{color:inherit;text-decoration:none;position:absolute;white-space:nowrap}
.nav .active{font-weight:700;color:var(--navy);border-bottom:2px solid var(--navy);padding-bottom:2px}
.quote-btn{left:910px;top:69px;width:178px;height:42px;border:2px solid var(--navy);color:var(--navy);font-family:"Libre Baskerville",serif;font-weight:700;font-size:13px;display:flex;align-items:center;justify-content:center;letter-spacing:.5px}

/* hero */
.hero-img{left:0;top:128px;width:1200px;height:592px;background:linear-gradient(100deg,#2a2e31 0%,#353838 40%,#5a4b3a 65%,#3a3f45 100%)}
.hero-text{left:112px;top:236px;color:var(--white)}
.hero-welcome{font-family:"Libre Baskerville",serif;font-size:18px}
.hero-title{font-family:"Libre Baskerville",serif;font-size:42px;margin-top:10px;line-height:48px;letter-spacing:.5px}
.hero-sub{font-family:"Libre Baskerville",serif;font-size:20px;letter-spacing:3px;margin-top:8px}
.hero-tag{font-size:17px;margin-top:14px}
.hero-copy{font-size:14.5px;line-height:30px;margin-top:16px;width:380px}
.btn-outline{border:2px solid var(--white);color:var(--white);font-family:"Libre Baskerville",serif;font-weight:700;font-size:13px;display:flex;align-items:center;justify-content:center;letter-spacing:.5px}
.hero-btn{left:112px;top:519px;width:150px;height:44px}

/* section heads */
.sec-title{left:0;width:1200px;text-align:center;color:var(--navy)}
.sec-lead{left:200px;width:800px;text-align:center;font-size:14.5px;line-height:30px;color:#333}

/* services */
.card{background:var(--white);box-shadow:0 2px 8px rgba(0,0,0,.12)}
.card.featured{border:2px solid var(--navy)}
.card-img{position:absolute;left:11px;top:8px;right:11px;height:280px}
.card-title{position:absolute;left:0;right:0;top:314px;text-align:center;font-family:"Libre Baskerville",serif;font-weight:700;font-size:14px;color:var(--ink)}
.featured .card-title{color:var(--navy);letter-spacing:1px}
.card-text{position:absolute;left:30px;right:30px;top:340px;text-align:center;font-size:13.5px;line-height:26px;color:#666}

/* about */
.about-title{left:620px;top:1650px;width:520px;color:var(--white);font-family:"Josefin Sans",sans-serif;font-weight:700;font-size:36px;line-height:47px;letter-spacing:1px}
.about-copy{left:620px;width:470px;color:var(--white);font-size:14.5px;line-height:31px}
.about-btn{left:622px;top:2006px;width:131px;height:40px}

/* team */
.member{background:var(--white);box-shadow:0 2px 10px rgba(0,0,0,.12);text-align:center}
.avatar{width:84px;height:84px;border-radius:50%;margin:30px auto 0}
.member-name{font-family:"Josefin Sans",sans-serif;font-weight:700;font-size:17px;margin-top:22px;letter-spacing:.5px}
.member-role{font-size:14px;margin-top:10px;color:#333}
.member-bio{font-size:13.5px;line-height:24px;color:#888;margin:12px 8px 0}
.member-social{display:flex;justify-content:center;gap:6px;margin-top:12px}
.ring{width:24px;height:24px;border-radius:50%;border:1px solid #bbb}

/* contact */
.contact-title{left:0;top:2903px;width:1200px;text-align:center;color:var(--white);font-family:"Josefin Sans",sans-serif;font-weight:700;font-size:38px;letter-spacing:2px}
.callback-title{left:110px;top:3016px;color:var(--white);font-family:"Josefin Sans",sans-serif;font-weight:700;font-size:31px;letter-spacing:1px}
.callback-copy{left:110px;width:440px;color:var(--white);font-size:14px;line-height:31px}
.social-fill{width:30px;height:30px;border-radius:50%;background:var(--navy)}
.contact-line{left:110px;color:var(--white);font-family:"Libre Baskerville",serif;font-weight:700;font-size:14px}
.form-box{left:633px;top:2981px;width:419px;height:510px;background:var(--white);border-top:5px solid var(--navy)}
.form-head{left:28px;top:42px;font-family:"Libre Baskerville",serif;font-weight:700;font-size:17px;color:var(--ink)}
.field{left:28px;width:362px;border-bottom:1px solid #ccc}
.field-label{font-size:14.5px;font-weight:700;color:#222}
.field-hint{font-size:11px;color:#bbb;margin-top:8px}
.field-icon{position:absolute;right:8px;top:26px;width:12px;height:12px}
.submit{left:28px;top:436px;width:128px;height:41px;border:2px solid var(--navy);color:var(--navy);font-family:"Libre Baskerville",serif;font-weight:700;font-size:12px;letter-spacing:1px;display:flex;align-items:center;justify-content:center}

/* footer */
.foot-brand{left:400px;top:3630px;width:400px;text-align:center;color:var(--navy)}
.foot-mark{width:48px;height:48px;background:var(--navy);margin:0 auto 22px}
.foot-name{font-family:"Libre Baskerville",serif;font-size:30px;line-height:36px}
.foot-tag{font-family:"Libre Baskerville",serif;font-size:12px;letter-spacing:3px;color:#888;margin-top:8px}
.foot-nav{top:3856px;font-family:"Libre Baskerville",serif;font-size:17px;color:var(--ink);white-space:nowrap;transform:translateX(-50%)}
.copyright{left:0;top:3927px;width:1200px;text-align:center;font-family:"Libre Baskerville",serif;font-size:13px;color:var(--ink)}
</style>
</head>
<body>

<!-- header -->
<svg class="abs topbar" width="1200" height="50" viewBox="0 0 1200 50">
  <polygon points="499,0 1200,0 1200,50 546,50" fill="#0b0a4f"/>
</svg>
<div class="abs top-rule"></div>
<div class="abs topbar-info">
  <span>&#9742; +1 888 888 8888</span><span class="sep">|</span>
  <span>&#9993; info@summitlinewealth.com</span><span class="sep">|</span>
  <span class="topbar-social"><i class="dot-s"></i><i class="dot-s"></i><i class="dot-s"></i><i class="dot-s"></i></span>
</div>
<div class="abs brand">
  <div class="brand-mark"></div>
  <div class="brand-name">SUMMITLINE WEALTH<br>MANAGEMENT</div>
</div>
<nav class="abs nav">
  <a class="active" style="left:0">HOME</a>
  <a style="left:79px">ABOUT US</a>
  <a style="left:193px">SERVICES</a>
  <a style="left:304px">TEAM</a>
  <a style="left:385px">CONTACT US</a>
</nav>
<div class="abs quote-btn">REQUEST A QUOTE</div>

<!-- hero -->
<div class="abs hero-img" role="img" aria-label="Hand holding stacks of coins beneath a rising growth chart with an upward arrow"></div>
<svg class="abs" style="left:0;top:600px" width="1200" height="130" viewBox="0 0 1200 130">
  <polygon points="0,120 540,65 1200,120 1200,130 0,130" fill="#fff"/>
  <polygon points="700,78 1200,0 1200,120" fill="#0b0a4f"/>
</svg>
<div class="abs hero-text">
  <div class="hero-welcome">WELCOME TO</div>
  <div class="hero-title">SUMMITLINE WEALTH</div>
  <div class="hero-sub">MANAGEMENT</div>
  <div class="hero-tag">GUIDING YOU TO YOUR FINANCIAL SUMMIT</div>
  <p class="hero-copy">Lorem ipsum dolor sit amet, consectetur adipiscing elit, sed do eiusmod tempor incididunt ut labore et dolore magna aliqua.</p>
</div>
<div class="abs btn-outline hero-btn">GET STARTED</div>

<!-- services -->
<h2 class="abs sec-title serif" style="top:758px;font-size:38px">OUR SERVICES</h2>
<p class="abs sec-lead" style="top:823px">Itaque earum rerum hic tenetur a sapiente delectus, ut aut reiciendis voluptatibus maiores alias consequatur aut perferendis doloribus asperiores repellat.</p>

<div class="abs card" style="left:112px;top:915px;width:317px;height:483px">
  <div class="card-img" role="img" aria-label="Smiling couple shaking hands with an advisor" style="background:linear-gradient(135deg,#7a6a5a,#b7a58f,#5c4d40)"></div>
  <div class="card-title">Financial Planning</div>
  <p class="card-text">Temporibus autem quibusdam et aut officiis debitis aut rerum necessitatibus saepe eveniet ut et voluptates repudiandae sint et molestiae non recusandae.</p>
</div>
<div class="abs card featured" style="left:443px;top:915px;width:314px;height:483px">
  <div class="card-img" role="img" aria-label="Coin stacks with rising blue arrows" style="background:linear-gradient(160deg,#0c2a4a,#1e6f9e,#0a1d33)"></div>
  <div class="card-title">INVESTMENT MANAGEMENT</div>
  <p class="card-text">Itaque earum rerum hic tenetur a sapiente delectus, ut aut reiciendis voluptatibus maiores alias consequatur aut perferendis doloribus asperiores repellat.</p>
</div>
<div class="abs card" style="left:771px;top:915px;width:317px;height:483px">
  <div class="card-img" role="img" aria-label="Hands on a laptop with glowing tax icons" style="background:linear-gradient(135deg,#6f6e72,#c9a27a,#3f3b3c)"></div>
  <div class="card-title">Tax Planning</div>
  <p class="card-text">Nam libero tempore, cum soluta nobis est eligendi optio cumque nihil impedit quo minus id quod maxime placeat facere possimus, omnis voluptas assumenda est, omnis dolor repellendus.</p>
</div>

<!-- about -->
<svg class="abs" style="left:0;top:1496px" width="1200" height="648" viewBox="0 0 1200 648">
  <polygon points="0,0 600,60 1200,10 1200,648 0,648" fill="#9c9c9c"/>
  <polygon points="0,110 1200,10 1200,648 0,648" fill="#0b0a4f"/>
</svg>
<div class="abs" role="img" aria-label="Laptop with a colourful growth bar chart" style="left:198px;top:1646px;width:313px;height:252px;background:linear-gradient(135deg,#1b3a6b,#3d7fb3,#c9d7e0)"></div>
<div class="abs" role="img" aria-label="Team of colleagues working together at a desk" style="left:145px;top:1862px;width:213px;height:208px;background:linear-gradient(135deg,#e7e3dc,#8b7f72,#f3f0ea)"></div>
<div class="abs" role="img" aria-label="Smiling businesswoman in an orange blazer" style="left:377px;top:1918px;width:167px;height:150px;background:linear-gradient(135deg,#efeae4,#c98a5c,#f4f1ee)"></div>
<h2 class="abs about-title">ABOUT SUMMITLINE WEALTH MANAGEMENT</h2>
<p class="abs about-copy" style="top:1747px">Nam libero tempore, cum soluta nobis est eligendi optio cumque nihil impedit quo minus id quod maxime placeat facere possimus, omnis ibus autem quibusdam et aut officiis debitis aut rerum necessitatibus saepe s repudiandae sint et molestiae non recusandae.</p>
<p class="abs about-copy" style="top:1902px">Itaque earum rerum hic tenetur a sapiente delectus, ut aut reiciendis voluptatibus maiores alias consequatur aut perferendis doloribus asperiores repellat.</p>
<div class="abs btn-outline about-btn">READ MORE</div>

<!-- team -->
<h2 class="abs sec-title josefin" style="top:2205px;font-size:38px;font-weight:600;letter-spacing:1px">OUR TEAM</h2>
<p class="abs sec-lead" style="top:2265px;left:220px;width:760px">Temporibus autem quibusdam et aut officiis debitis aut rerum necessitatibus saepe eveniet ut et voluptates repudiandae sint et molestiae non recusandae.</p>

<div class="abs member" style="left:112px;top:2353px;width:221px;height:331px">
  <div class="avatar" role="img" aria-label="Portrait of John Smith" style="background:#c9c3bd"></div>
  <div class="member-name">JOHN SMITH</div><div class="member-role">Founder</div>
  <p class="member-bio">Sed ut perspiciatis unde omnis iste natus er ror sit voluptatem accusantium dolorea.</p>
  <div class="member-social"><i class="ring"></i><i class="ring"></i><i class="ring"></i></div>
</div>
<div class="abs member" style="left:363px;top:2353px;width:221px;height:331px">
  <div class="avatar" role="img" aria-label="Portrait of Allen Miller" style="background:#3a3c45"></div>
  <div class="member-name">ALLEN MILLER</div><div class="member-role">Director</div>
  <p class="member-bio">Itaque earum rerum hic tenetur a sapiente delectus, ut aut reiciendis voluptatibus</p>
  <div class="member-social"><i class="ring"></i><i class="ring"></i><i class="ring"></i></div>
</div>
<div class="abs member" style="left:616px;top:2353px;width:221px;height:331px">
  <div class="avatar" role="img" aria-label="Portrait of Anna Dunn" style="background:#b58f72"></div>
  <div class="member-name">ANNA DUNN</div><div class="member-role">Assistant Director</div>
  <p class="member-bio">Sed ut perspiciatis unde omnis iste natus er ror sit volupta tem accusantium</p>
  <div class="member-social"><i class="ring"></i><i class="ring"></i><i class="ring"></i></div>
</div>
<div class="abs member" style="left:866px;top:2353px;width:222px;height:331px">
  <div class="avatar" role="img" aria-label="Portrait of the manager" style="background:#2d3540"></div>
  <div class="member-name">ALLEN MILLER</div><div class="member-role">Manager</div>
  <p class="member-bio">Earum rerum hic tenetur a sapiente delectus, ut aut reiciendis voluptatibus</p>
  <div class="member-social"><i class="ring"></i><i class="ring"></i><i class="ring"></i></div>
</div>

<!-- contact -->
<svg class="abs" style="left:0;top:2774px" width="1200" height="782" viewBox="0 0 1200 782">
  <rect width="1200" height="782" fill="#9c9c9c"/>
  <polygon points="560,62 1200,0 1200,110" fill="#0b0a4f"/>
</svg>
<h2 class="abs contact-title">GET IN TOUCH WITH US</h2>
<h3 class="abs callback-title">REQUEST A CALL BACK</h3>
<p class="abs callback-copy" style="top:3066px">Nam libero tempore, cum soluta nobis est eligendi optio cumque nihil impedit quo minus id quod maxime placeat facere possimus, omnis voluptas assumenda est, omnis dolor repellendus.</p>
<p class="abs callback-copy" style="top:3189px">Temporibus autem quibusdam et aut officiis debitis aut rerum necessitatibus saepe eveniet ut et voluptates repudiandae sint et molestiae non recusandae.</p>
<div class="abs" style="left:111px;top:3301px;display:flex;gap:28px"><i class="social-fill"></i><i class="social-fill"></i><i class="social-fill"></i><i class="social-fill"></i></div>
<div class="abs contact-line" style="top:3362px">Location: Summitline Wealth Management, United States</div>
<div class="abs contact-line" style="top:3400px">Call Us: +1 888 888 8888</div>
<div class="abs contact-line" style="top:3438px">Mail Us: info@summitlinewealth.com</div>

<div class="abs form-box">
  <div class="abs form-head">DROP YOUR MESSAGE</div>
  <div class="abs field" style="top:86px;height:57px"><div class="field-label">Name</div><div class="field-hint">Jacob Mason</div>
    <svg class="field-icon" viewBox="0 0 12 12"><circle cx="6" cy="3.5" r="2.5" fill="#aaa"/><path d="M1 12a5 5 0 0 1 10 0z" fill="#aaa"/></svg></div>
  <div class="abs field" style="top:157px;height:57px"><div class="field-label">Email</div><div class="field-hint">Jacobmason@mail.com</div>
    <svg class="field-icon" viewBox="0 0 12 12"><rect x="0.5" y="2.5" width="11" height="7" fill="none" stroke="#aaa"/><path d="M0.5 2.5 6 7 11.5 2.5" fill="none" stroke="#aaa"/></svg></div>
  <div class="abs field" style="top:228px;height:56px"><div class="field-label">Phone Number</div><div class="field-hint">+123 ........</div>
    <svg class="field-icon" viewBox="0 0 12 12"><path d="M2 1l2 0 1 3-1.5 1a7 7 0 0 0 3.5 3.5L8 7l3 1v2l-1 1A10 10 0 0 1 1 2z" fill="none" stroke="#aaa"/></svg></div>
  <div class="abs field" style="top:316px;height:89px"><div class="field-label">Message</div><div class="field-hint">Type Your Message</div>
    <svg class="field-icon" viewBox="0 0 12 12"><ellipse cx="6" cy="5" rx="5.5" ry="4" fill="#aaa"/><path d="M2 8l-1 3 4-2z" fill="#aaa"/></svg></div>
  <div class="abs submit">SUBMIT</div>
</div>

<!-- footer -->
<div class="abs foot-brand">
  <div class="foot-mark"></div>
  <div class="foot-name">SUMMITLINE WEALTH<br>MANAGEMENT</div>
  <div class="foot-tag">GUIDING YOU TO YOUR FINANCIAL SUMMIT</div>
</div>
<div class="abs foot-nav" style="left:319px">HOME</div>
<div class="abs foot-nav" style="left:438px">ABOUT US</div>
<div class="abs foot-nav" style="left:584px">SERVICES</div>
<div class="abs foot-nav" style="left:709px">TEAM</div>
<div class="abs foot-nav" style="left:849px">CONTACT US</div>
<div class="abs copyright">COPYRIGHTS@2024.SUMMITLINE WEALTH.ALL RIGHTS RESERVED</div>

</body>
</html>
```